Home Health Care Agency Needs a Website (Seeking a PSD)

We need a user friendly website for a Home Health Care Agency. Our service is for the elderly and disabled. Frequently the busy professional middle-aged married daughter will use the website to arrange in-home care for an aging parent. Therefore, our website is primarily geared towards middle-aged women. In-home care is typically 24 hours a day so, a feeling of trustworthiness and security should be effectively conveyed. (Seeking a PSD- however, if you also offer coding, please let us know the cost.)

Target Market(s)

Frequently the busy professional middle-aged married daughter (possibly out of state) will use the website to arrange in-home care for an aging parent.

Industry/Entity Type

Security

Requirements
Must have
• Website must be clean, uncluttered and professional. The following menu pages are requested: Home, About Us, Services, Resources, FAQ, Employment & Contact.
Should not have
• Must not be too whimsical.

```html
<!DOCTYPE html>
<html lang="en">
<head>
<meta charset="utf-8">
<title>Haven Home Health – Home Health Care Agency</title>
<link href="https://fonts.googleapis.com/css2?family=Nunito+Sans:wght@400;600;700;800&display=swap" rel="stylesheet">
<style>
:root{
  --blue:#47c4ee;
  --blue-dark:#2fb3e2;
  --slate:#5f6067;
  --green:#bccd5f;
  --footer:#7b7c81;
  --ink:#3a3a3d;
  --muted:#6b6b70;
  --rule:#c9c9cc;
  --white:#ffffff;
}
*{margin:0;padding:0;box-sizing:border-box}
html,body{width:1200px;height:1026px;overflow:hidden;background:var(--white)}
body{position:relative;font-family:"Nunito Sans",Arial,sans-serif;color:var(--ink)}
.abs{position:absolute}

.top-rule{left:0;top:0;width:1200px;height:2px;background:var(--blue)}
.header-bg{left:0;top:2px;width:1200px;height:95px;background:linear-gradient(90deg,#f1f5f8,#fff 20%,#fff 80%,#f1f5f8)}
.brand{left:196px;top:22px;display:flex;align-items:center;gap:8px}
.brand-dot{width:26px;height:26px;border-radius:50%;background:var(--blue)}
.brand-name{font-weight:800;font-size:21px;line-height:21px;color:var(--blue)}

.callout{left:792px;top:26px;width:210px;height:56px}
.callout svg{position:absolute;left:0;top:18px}
.callout-label{position:absolute;left:34px;top:0;font-weight:700;font-size:13px;line-height:16px;color:var(--slate);white-space:nowrap}
.callout-number{position:absolute;left:33px;top:14px;font-size:22px;line-height:24px;font-weight:600;color:var(--blue);letter-spacing:0;white-space:nowrap}
.callout-hours{position:absolute;left:35px;top:39px;font-size:11.5px;line-height:14px;color:var(--slate);letter-spacing:.3px;white-space:nowrap}

.nav-line{left:0;top:96px;width:1200px;height:1px;background:#eceef0}
.main-nav{left:193px;top:103px;height:32px;display:flex}
.main-nav a{display:block;height:32px;line-height:32px;font-size:11px;color:var(--slate);text-decoration:none;text-transform:uppercase;letter-spacing:.2px}
.main-nav a.current{background:var(--blue);color:var(--white);padding:0 14px}
.search{left:793px;top:105px;width:201px;height:29px;border:1px solid #cfd2d5;background:#fff}
.search svg{position:absolute;left:8px;top:6px}
.search-sep{position:absolute;left:36px;top:6px;height:16px;border-left:1px dotted #999}
.search-label{position:absolute;left:47px;top:7px;font-size:11px;color:var(--slate)}

.hero-band-top{left:0;top:139px;width:1200px;height:192px;background:var(--blue)}
.hero-band-bottom{left:0;top:331px;width:1200px;height:176px;background:var(--slate)}
.hero-photo{left:94px;top:139px;width:1000px;height:384px;background:linear-gradient(110deg,#dfe3e8 0%,#c9d0d8 25%,#e8d7cc 45%,#a9cfe4 65%,#66b8de 100%)}
.hero-caption{left:528px;top:342px;width:448px;height:88px;background:var(--green);color:var(--white);padding:10px 15px;overflow:hidden}
.hero-caption h1{font-weight:700;font-size:29px;line-height:34px;letter-spacing:-.9px;white-space:nowrap}
.hero-caption p{font-size:12.5px;line-height:14px;margin-top:4px}
.btn-hero{top:434px;height:40px;line-height:40px;text-align:center;color:var(--white);font-weight:600;font-size:22px;letter-spacing:-.3px}
.btn-learn{left:528px;width:180px;background:var(--blue)}
.btn-join{left:711px;width:148px;background:var(--slate)}
.slider-dots{left:926px;top:501px;display:flex;gap:4px}
.slider-dots span{width:11px;height:11px;border-radius:50%;background:#e9f6fc}
.slider-dots span.on{background:var(--blue)}
.hero-shadow{left:140px;top:523px;width:920px;height:12px;background:radial-gradient(ellipse at top,rgba(0,0,0,.12),transparent 70%)}

.service{top:562px;width:194px}
.service h2{font-size:15.5px;font-weight:700;display:flex;align-items:center;gap:10px;white-space:nowrap}
.service h2::after{content:"";flex:1;border-bottom:1px dotted #9a9a9e;margin-top:4px}
.service.blue h2{color:var(--blue)}
.service.gray h2{color:var(--slate)}
.service .frame{margin-top:11px;width:194px;height:112px;border:1px solid #e1e1e3;padding:4px;background:#fff;box-shadow:0 6px 6px -5px rgba(0,0,0,.15)}
.service .frame div{width:100%;height:100%}
.service p{margin-top:14px;font-size:9.5px;line-height:12px;color:var(--ink);padding-left:2px}

.info-band{left:0;top:770px;width:1200px;height:212px;background:var(--blue);color:var(--white)}
.welcome{left:195px;top:802px;width:380px}
.welcome h2{font-weight:800;font-size:31px;line-height:34px;display:flex;align-items:center;gap:14px}
.welcome h2::after{content:"";flex:1;border-bottom:1px dotted rgba(255,255,255,.6);margin-top:6px}
.welcome h3{font-weight:400;font-size:12.5px;margin-top:5px}
.welcome p{font-size:9px;line-height:11.7px;margin-top:9px;opacity:.95}
.btn-read{display:inline-block;margin-top:9px;margin-left:1px;width:54px;height:25px;line-height:22px;text-align:center;border:2px solid var(--white);font-weight:700;font-size:11px}
.band-divider{left:597px;top:810px;height:126px;border-left:1px dotted rgba(255,255,255,.6)}
.stories-title{left:624px;top:805px;width:312px;font-weight:600;font-size:21px;display:flex;align-items:center;gap:12px;white-space:nowrap}
.stories-title::after{content:"";flex:1;border-bottom:1px dotted rgba(255,255,255,.6);margin-top:5px}
.stories-arrows{left:952px;top:808px;display:flex;gap:2px}
.avatar{left:620px;top:852px;width:77px;height:77px;border-radius:50%;border:4px solid #fff;background:radial-gradient(circle at 50% 40%,#d9b9a3,#6d4e3f 70%,#e6eaee 71%);box-shadow:0 2px 4px rgba(0,0,0,.15)}
.quote-mark{font-size:40px;font-weight:800;line-height:1;color:rgba(255,255,255,.55)}
.quote-open{left:698px;top:852px}
.quote-close{left:860px;top:896px}
.story{left:726px;top:863px;width:268px;font-size:9px;line-height:12.5px}
.story-name{left:728px;top:930px;font-weight:700;font-size:10px}

.footer{left:0;top:984px;width:1200px;height:42px;background:var(--footer);color:#e3e3e5;font-size:9.5px}
.footer .copy{position:absolute;left:196px;top:16px}
.footer nav{position:absolute;right:209px;top:16px;letter-spacing:.3px}
</style>
</head>
<body>

<div class="abs top-rule"></div>
<div class="abs header-bg"></div>

<div class="abs brand">
  <span class="brand-dot"></span>
  <span class="brand-name">Haven<br>Home Health</span>
</div>

<div class="abs callout">
  <svg width="30" height="32" viewBox="0 0 30 32" aria-hidden="true"><path d="M7 2c2 0 3 1 4 4l1 4c.5 2-1 3-2 4 1 3 4 7 7 9 1-1 2-2.5 4-2l4 2c2 1 3 2 3 4l-2 3c-2 2-5 2-8 1C11 28 4 20 2 11 1 7 2 4 5 2.5z" fill="#404145"/></svg>
  <div class="callout-label">CALL US TODAY</div>
  <div class="callout-number">1-800-555-0142</div>
  <div class="callout-hours">OPEN 24/7 - 7 DAYS A WEEK</div>
</div>

<div class="abs nav-line"></div>
<nav class="abs main-nav">
  <a class="current" href="#">Home</a>
  <a href="#" style="margin-left:14px">About Us</a>
  <a href="#" style="margin-left:36px">Services</a>
  <a href="#" style="margin-left:36px">Resources</a>
  <a href="#" style="margin-left:36px">FAQ</a>
  <a href="#" style="margin-left:36px">Employment</a>
  <a href="#" style="margin-left:38px">Contact</a>
</nav>
<div class="abs search">
  <svg width="18" height="18" viewBox="0 0 18 18" aria-hidden="true"><circle cx="7" cy="7" r="5.5" fill="none" stroke="#333" stroke-width="1.8"/><line x1="11" y1="11" x2="16.5" y2="16.5" stroke="#333" stroke-width="2.2"/></svg>
  <span class="search-sep"></span>
  <span class="search-label">SEARCH</span>
</div>

<div class="abs hero-band-top"></div>
<div class="abs hero-band-bottom"></div>
<div class="abs hero-photo" role="img" aria-label="Nurse in blue scrubs smiling at an elderly woman resting in bed"></div>
<div class="abs hero-shadow"></div>
<div class="abs hero-caption">
  <h1>HOME HEALTH CARE AGENCY</h1>
  <p>Our core values are based on fundamentals of Respect, Dignity, Integrity and Compassion,</p>
</div>
<div class="abs btn-hero btn-learn">LEARN MORE</div>
<div class="abs btn-hero btn-join">JOIN US</div>
<div class="abs slider-dots"><span class="on"></span><span></span><span></span><span></span></div>

<section class="abs service blue" style="left:193px">
  <h2>HOME CARE</h2>
  <div class="frame"><div role="img" aria-label="Caregiver with an elderly woman at home" style="background:linear-gradient(100deg,#f2ece6,#e4d6ca 50%,#eef1f4)"></div></div>
  <p>Lorem ipsum dolor sit amet, consectetuer adipiscing elit,</p>
</section>
<section class="abs service gray" style="left:395px">
  <h2>HOSPICE</h2>
  <div class="frame"><div role="img" aria-label="Smiling elderly couple" style="background:linear-gradient(100deg,#9fb8c9,#d9b8a3 45%,#c9b89a)"></div></div>
  <p>Lorem ipsum dolor sit amet, consectetuer adipiscing elit,</p>
</section>
<section class="abs service blue" style="left:597px">
  <h2>DAY CARE</h2>
  <div class="frame"><div role="img" aria-label="Nurse assisting an elderly man" style="background:linear-gradient(100deg,#e8e4de,#c9c4bd 50%,#b9c7d4)"></div></div>
  <p>Lorem ipsum dolor sit amet, consectetuer adipiscing elit,</p>
</section>
<section class="abs service gray" style="left:800px">
  <h2>OUR CAREGIVERS</h2>
  <div class="frame"><div role="img" aria-label="Caregiver embracing an elderly woman" style="background:linear-gradient(100deg,#e7e2d6,#e0c3ad 50%,#3c4a66)"></div></div>
  <p>Lorem ipsum dolor sit amet, consectetuer adipiscing elit,</p>
</section>

<div class="abs info-band"></div>
<section class="abs welcome" style="color:#fff">
  <h2>WELCOME</h2>
  <h3>Experienced Care, Delivered with Love!</h3>
  <p>Lorem ipsum dolor sit amet, consectetuer adipiscing elit, sed diam nonummy nibh euismod tincidunt ut laoreet dolore magna aliquam erat volutpat. Ut wisi enim ad minim veniam, quis nostrud exerci tation ullamcorper suscipit lobortis nisl ut aliquip ex ea commodo consequat. Duis autem vel eum iriure dolor in hendrerit in vulputate velit esse molestie consequat, vel illum dolore eu feugiat nulla facilisiS.</p>
  <span class="btn-read">Read</span>
</section>
<div class="abs band-divider"></div>

<h2 class="abs stories-title" style="color:#fff">FAMILY STORIES</h2>
<div class="abs stories-arrows">
  <svg width="42" height="20" viewBox="0 0 42 20" aria-hidden="true">
    <circle cx="10" cy="10" r="9.5" fill="#8bd8f3"/><path d="M12 5l-5 5 5 5" fill="none" stroke="#fff" stroke-width="2.2"/>
    <circle cx="32" cy="10" r="9.5" fill="#8bd8f3"/><path d="M30 5l5 5-5 5" fill="none" stroke="#fff" stroke-width="2.2"/>
  </svg>
</div>
<div class="abs avatar" role="img" aria-label="Portrait of a family member"></div>
<div class="abs quote-mark quote-open">&ldquo;</div>
<p class="abs story" style="color:#fff">Duis autem vel eum iriure dolor in hendrerit in vulputate velit esse molestie consequat, vel illum dolore eu feugiat nulla facilisis at vero eros et accumsan et iusto odio dignissim qui blandit praesent luptatum zzril</p>
<div class="abs quote-mark quote-close">&rdquo;</div>
<div class="abs story-name" style="color:#fff">- Laura M.</div>

<footer class="abs footer">
  <span class="copy">© 2013 Haven Home Health. All rights reserved.</span>
  <nav>HOME - ABOUT US - SERVICES - RESOURCES - FAQ - EMPLOYMENT - CONTACT</nav>
</footer>

</body>
</html>
```